Consulting company needs Business Cards - rough concept provided

I'm looking for someone to take our business card idea and make is slick and polished - to communicate our high-end, sophisticated, serious consulting business. We have a rough layout we did in-house. We are open to ideas on repo-ing elements, adjusting sizes, typefaces etc... within the general concept we've already come up with. We want it to be super-clean and sophisticated. We want to keep the white backgrounds, and blue brand colors. Our goal is to print with painted blue edges on thick cardstock. Thank you!!

```html
<!DOCTYPE html>
<html lang="en">
<head>
<meta charset="utf-8">
<title>Norvale Stationery Set</title>
<link rel="stylesheet" href="https://fonts.googleapis.com/css2?family=Roboto:wght@400;500;700&display=swap">
<style>
  :root {
    --brand-blue: #1a7cc4;
    --brand-blue-deep: #0d5d9e;
    --brand-blue-light: #4aa6e0;
    --brand-blue-fade: rgba(26, 124, 196, 0);
    --paper: #ffffff;
    --backdrop: #eef0f2;
    --rule: #b9bdc2;
    --ink: #1d1f22;
    --ink-soft: #3a3d42;
  }
  * { box-sizing: border-box; margin: 0; padding: 0; }
  html, body { width: 1200px; height: 1200px; overflow: hidden; }
  body {
    position: relative;
    background: var(--backdrop);
    font-family: "Roboto", Arial, sans-serif;
    color: var(--ink);
  }
  .piece {
    position: absolute;
    background: var(--paper);
    overflow: hidden;
  }
  .wordmark {
    font-family: "Roboto", Arial, sans-serif;
    font-weight: 700;
    color: var(--brand-blue);
    letter-spacing: 0.02em;
    line-height: 1;
    white-space: nowrap;
  }
  .ribbon-area { position: absolute; }
  .contact-line {
    position: absolute;
    font-size: 10px;
    color: var(--ink-soft);
    text-align: center;
    white-space: nowrap;
  }
  .contact-line .sep { margin: 0 6px; color: var(--rule); }
  .hairline {
    position: absolute;
    height: 2px;
    background: linear-gradient(90deg, #d6d9dc, #a9adb2 50%, #d6d9dc);
  }

  /* Letterhead */
  .letterhead { left: 78px; top: 117px; width: 505px; height: 683px; }
  .letterhead .wordmark { position: absolute; top: 36px; right: 30px; font-size: 32px; }
  .letterhead .ribbon-area {
    left: 0; top: 0; width: 280px; height: 340px;
    background: linear-gradient(160deg, var(--brand-blue) 0%, rgba(26,124,196,0.55) 35%, var(--brand-blue-fade) 75%);
  }
  .letterhead .hairline { left: 30px; right: 30px; top: 638px; }
  .letterhead .contact-line { left: 0; right: 0; top: 652px; }

  /* Envelope front */
  .envelope-front { left: 630px; top: 115px; width: 489px; height: 280px; }
  .envelope-front .wordmark { position: absolute; left: 30px; top: 34px; font-size: 30px; }
  .envelope-front .address-window {
    position: absolute; left: 244px; top: 128px; width: 215px; height: 100px;
    border: 1px solid #d4d7da; border-radius: 10px; background: #f7f8f9;
  }
  .envelope-front .hairline { left: 30px; right: 30px; top: 252px; }

  /* Envelope back */
  .envelope-back { left: 630px; top: 443px; width: 489px; height: 295px; }
  .envelope-back .flaps { position: absolute; inset: 0; }
  .envelope-back .ribbon-area {
    left: 0; top: 0; width: 489px; height: 190px;
    background: linear-gradient(200deg, var(--brand-blue) 0%, rgba(26,124,196,0.5) 40%, var(--brand-blue-fade) 80%);
  }
  .envelope-back .hairline { left: 50px; right: 50px; top: 250px; }
  .envelope-back .contact-line { left: 0; right: 0; top: 260px; font-size: 9.5px; }

  /* Business cards */
  .card { box-shadow: 0 0 0 3px var(--brand-blue); }
  .card-front {
    left: 182px; top: 860px; width: 385px; height: 218px;
    display: flex; align-items: center; justify-content: center;
  }
  .card-front .wordmark { font-size: 48px; }

  .card-back {
    left: 642px; top: 860px; width: 385px; height: 218px;
    background: linear-gradient(135deg, var(--brand-blue-deep), var(--brand-blue) 55%, var(--brand-blue-light));
  }
  .card-back .info-panel {
    position: absolute; left: 24px; top: 20px; right: 24px; bottom: 20px;
    background: var(--paper);
    border: 1px solid #9fa4a9;
    box-shadow: inset 0 0 0 5px var(--paper), inset 0 0 0 6px #c3c7cb;
    display: flex; flex-direction: column; align-items: center; justify-content: center;
    text-align: center;
  }
  .card-back .person-name { font-size: 19px; font-weight: 500; color: var(--ink); }
  .card-back .person-role { font-size: 11px; color: var(--ink-soft); margin-top: 2px; }
  .card-back .panel-rule { width: 190px; height: 1px; background: var(--rule); margin: 8px 0; }
  .card-back .service-line { font-size: 11.5px; font-weight: 500; color: var(--ink); }
  .card-back .contact-stack { font-size: 11px; color: var(--ink); line-height: 1.4; }
</style>
</head>
<body>

  <section class="piece letterhead">
    <div class="ribbon-area" role="img" aria-label="Area for the flowing blue ribbon artwork"></div>
    <div class="wordmark">NORVALE</div>
    <div class="hairline"></div>
    <p class="contact-line">+1 (555) 010-2384<span class="sep">|</span>info@norvale.com<span class="sep">|</span>42 Harbour Lane, London, UK</p>
  </section>

  <section class="piece envelope-front">
    <div class="wordmark">NORVALE</div>
    <div class="address-window"></div>
    <div class="hairline"></div>
  </section>

  <section class="piece envelope-back">
    <svg class="flaps" viewBox="0 0 489 295" aria-hidden="true">
      <path d="M0 295 L200 175 M489 295 L290 175" stroke="#dcdfe2" stroke-width="1.5" fill="none"/>
      <path d="M0 0 L220 175 Q244 190 268 175 L489 0" stroke="#c9cdd1" stroke-width="1.5" fill="#fbfbfc"/>
    </svg>
    <div class="ribbon-area" role="img" aria-label="Area for the flowing blue ribbon artwork"></div>
    <div class="hairline"></div>
    <p class="contact-line">+1 (555) 010-2384<span class="sep">|</span>info@norvale.com<span class="sep">|</span>42 Harbour Lane, London, UK</p>
  </section>

  <section class="piece card card-front">
    <div class="wordmark">NORVALE</div>
  </section>

  <section class="piece card card-back" role="img" aria-label="Blue card face with ribbon artwork around a white information panel">
    <div class="info-panel">
      <p class="person-name">Marcus Ellery</p>
      <p class="person-role">Principal Consultant</p>
      <div class="panel-rule"></div>
      <p class="service-line">Consulting Services</p>
      <div class="panel-rule"></div>
      <p class="contact-stack">+1 (555) 010-2384<br>info@norvale.com<br>42 Harbour Lane, London, UK</p>
    </div>
  </section>

</body>
</html>
```